A3 Menus for new international restaurant in Singapore.

Looking for new A3 menu design for indoor & outdoor (beautiful garden and trees) restaurant that caters for expat and local families. International menu, cool jazz vibe, great for couples and families. Restaurant called Brass Cove Parlour. I have attached some of the logos we use. Will consider black and white or color options. Restaurant located on a hill where there were tin mines many years ago, hence the name and branding. Looking for three menus (1) Dinner (2) Lunch (3) weekend brunch.

Target Market(s)

Families, young couples and professionals.

Industry/Entity Type

Restaurant

Font styles to use
Serif
Sans Serif

Requirements
Must have
• All food layout on one side of A3, one for each attached menu. Also a space for drinks list on the back.
Nice to have
• Use some of the logo material we have attached.
Should not have

```html
<!DOCTYPE html>
<html lang="en">
<head>
<meta charset="utf-8">
<title>Brass Cove Parlour – Menu Suite</title>
<link rel="stylesheet" href="https://fonts.googleapis.com/css2?family=Special+Elite&family=Cinzel:wght@400;700&family=Rye&display=swap">
<style>
  :root {
    --backdrop: #2e2824;
    --rust-deep: #7a3514;
    --rust-mid: #b85a22;
    --rust-light: #d98a4a;
    --rust-pale: #e6b98a;
    --tin-grey: #b9b4ad;
    --band-brown: #5a2f14;
    --ink: #2b231e;
    --accent-orange: #c8642a;
    --paper: #fbfaf7;
    --cream: #f4eadb;
    --faint-disc: rgba(240, 210, 190, 0.35);
  }
  * { box-sizing: border-box; margin: 0; padding: 0; }
  html, body { width: 1200px; height: 1000px; overflow: hidden; }
  body {
    background: var(--backdrop);
    font-family: "Special Elite", "Courier New", monospace;
    color: var(--ink);
  }
  .suite {
    width: 1200px; height: 1000px;
    display: grid;
    grid-template-columns: repeat(2, 340px);
    grid-template-rows: repeat(2, 470px);
    gap: 20px 40px;
    justify-content: center;
    align-content: center;
  }
  .menu {
    position: relative;
    overflow: hidden;
    box-shadow: 0 6px 18px rgba(0,0,0,0.45);
  }
  .rust {
    position: absolute; inset: 0;
    background:
      radial-gradient(circle at 22% 30%, var(--rust-deep) 0 8%, transparent 20%),
      radial-gradient(circle at 70% 18%, var(--rust-mid) 0 10%, transparent 28%),
      radial-gradient(circle at 40% 70%, var(--rust-deep) 0 6%, transparent 22%),
      radial-gradient(circle at 85% 60%, var(--tin-grey) 0 10%, transparent 30%),
      radial-gradient(circle at 10% 85%, var(--tin-grey) 0 8%, transparent 26%),
      linear-gradient(135deg, var(--rust-light), var(--rust-mid) 45%, var(--rust-pale) 75%, var(--rust-mid));
  }
  .disc {
    position: absolute;
    width: 70px; height: 70px;
    border-radius: 50%;
    background: var(--faint-disc);
  }
  .menu-tab {
    position: absolute; top: 0; left: 0; right: 0;
    height: 24px;
    background: var(--band-brown);
    color: var(--cream);
    font-family: "Cinzel", Georgia, serif;
    font-weight: 700;
    font-size: 12px;
    letter-spacing: 0.45em;
    text-transform: uppercase;
    display: flex; align-items: center; justify-content: flex-end;
    padding-right: 14px;
  }
  .brand {
    position: absolute; top: 40px; left: 0; right: 0;
    display: flex; align-items: center; justify-content: center; gap: 10px;
  }
  .brand-mark {
    width: 14px; height: 14px; border-radius: 50%;
    background: var(--ink);
  }
  .brand-name {
    font-family: "Special Elite", "Courier New", monospace;
    font-size: 24px;
    color: var(--ink);
    text-transform: uppercase;
    line-height: 1;
    text-align: center;
  }
  .sheet {
    position: absolute; left: 22px; right: 22px; top: 100px; bottom: 18px;
    background: var(--paper);
    box-shadow: 0 0 6px rgba(60,30,10,0.35);
    padding: 12px 14px;
    font-size: 7.6px;
    line-height: 1.35;
  }
  .section-title {
    font-family: "Rye", Georgia, serif;
    color: var(--accent-orange);
    font-size: 12px;
    text-transform: uppercase;
    text-align: center;
    margin: 4px 0 4px;
  }
  .dish { margin-bottom: 5px; text-align: center; }
  .dish-name { text-transform: uppercase; font-size: 8px; }
  .rule { border: 0; border-top: 1px dashed var(--accent-orange); margin: 6px 10px; }

  /* Libations cover */
  .menu--libations .brand { top: 70px; flex-direction: column; gap: 8px; }
  .menu--libations .brand-name { font-size: 38px; line-height: 1.05; }
  .menu--libations .menu-label {
    position: absolute; top: 200px; left: 0; right: 0;
    text-align: center;
    font-family: "Cinzel", Georgia, serif;
    color: var(--cream);
    font-size: 15px;
    letter-spacing: 0.5em;
  }
  .menu--libations .sheet { top: 240px; left: 70px; right: 50px; bottom: 0; }
</style>
</head>
<body>
<main class="suite">

  <article class="menu menu--libations">
    <div class="rust" role="img" aria-label="Rusted tin sheet texture"></div>
    <div class="disc" style="top:28px; right:26px" role="img" aria-label="Faint fork emblem"></div>
    <div class="disc" style="bottom:30px; left:14px" role="img" aria-label="Faint jug emblem"></div>
    <div class="brand">
      <span class="brand-mark"></span>
      <span class="brand-name">Brass Cove<br>Parlour</span>
    </div>
    <p class="menu-label">LIBATIONS</p>
    <div class="sheet"></div>
  </article>

  <article class="menu menu--dinner">
    <div class="rust" role="img" aria-label="Rusted tin sheet texture"></div>
    <header class="menu-tab">Dinner Menu</header>
    <div class="brand"><span class="brand-mark"></span><span class="brand-name">Brass Cove Parlour</span></div>
    <div class="sheet">
      <h2 class="section-title">Platters</h2>
      <div class="dish"><span class="dish-name">Seafood Platter</span><br>selection of gravlax, smoked fish, marinated seafood, pumpernickel bread and dipping sauces<br>$38 for 2 to share / $70 for 4 to share</div>
      <div class="dish"><span class="dish-name">Charcuterie Platter</span><br>3 types of charcuterie, duck rillettes, pickles, crostini and wholegrain mustard<br>$32 for 2 to share / $60 for 4 to share</div>
      <hr class="rule">
      <h2 class="section-title">Starters</h2>
      <div class="dish"><span class="dish-name">Roasted Red Capsicum Soup</span> with peppered cream $12</div>
      <div class="dish"><span class="dish-name">Beef Tartare</span> hand-chopped with capers, pickles and shallots $18</div>
      <hr class="rule">
      <h2 class="section-title">Main Courses</h2>
      <div class="dish"><span class="dish-name">Brass Cove Parlour Burger</span> $24 &nbsp; <span class="dish-name">Roast Chicken</span> $28</div>
      <div class="dish"><span class="dish-name">Crispy Pork Belly</span> with parsnip mash and apple $29</div>
    </div>
  </article>

  <article class="menu menu--brunch">
    <div class="rust" role="img" aria-label="Rusted tin sheet texture"></div>
    <header class="menu-tab">Brunch Menu</header>
    <div class="brand"><span class="brand-mark"></span><span class="brand-name">Brass Cove Parlour</span></div>
    <div class="sheet">
      <div class="dish"><span class="dish-name">Brass Cove Parlour Muesli and Yoghurt</span> with fruit compote $9.50</div>
      <div class="dish"><span class="dish-name">Waffle</span> served with mixed fruit, maple syrup and crushed nuts $14</div>
      <div class="dish"><span class="dish-name">Scrambled Eggs</span> on sour dough toast, with roast tomato, portobello mushroom and chives $13.50</div>
      <div class="dish"><span class="dish-name">Baked Gypsy Eggs</span> with rustic napolitano sauce, peas and diced pan-fried potato $15.50</div>
      <div class="dish"><span class="dish-name">Brass Cove Parlour Benedict</span> poached eggs served with either pulled pork or smoked salmon, on sour dough toast $16</div>
      <hr class="rule">
      <h2 class="section-title">The Hearty Plates</h2>
      <div class="dish"><span class="dish-name">Full Parlour Breakfast</span> eggs, bacon, sausage, beans and toast $19</div>
      <div class="dish"><span class="dish-name">Corn Fritters</span> with avocado salsa and sour cream $15</div>
    </div>
  </article>

  <article class="menu menu--lunch">
    <div class="rust" role="img" aria-label="Rusted tin sheet texture"></div>
    <header class="menu-tab">Lunch Menu</header>
    <div class="brand"><span class="brand-mark"></span><span class="brand-name">Brass Cove Parlour</span></div>
    <div class="sheet">
      <div class="dish"><span class="dish-name">Brass Cove Parlour Muesli and Yoghurt</span> with fruit compote $9.50</div>
      <div class="dish"><span class="dish-name">Scrambled Eggs</span> on sour dough toast, with roast tomato and chives $13.50</div>
      <h2 class="section-title">Russian Salad</h2>
      <div class="dish">with tuna and smoked salmon, carrots, peas, hardboiled farm eggs and potato with a choice of vinaigrette or mayonnaise dressing $15.50</div>
      <hr class="rule">
      <div class="dish"><span class="dish-name">Classic Greek Salad</span> with cherry tomatoes, feta, kalamata olives and cucumber $14.50</div>
      <div class="dish"><span class="dish-name">Arugula Salad</span> with goat's cheese, hazelnuts and honey mustard dressing $12</div>
      <div class="dish"><span class="dish-name">Strozzi</span> with beef ragu bolognese $16</div>
      <div class="dish"><span class="dish-name">Linguini</span> in a light creamy carbonara sauce with smoked pancetta $17</div>
      <div class="dish"><span class="dish-name">Roast Pork Belly Ciabatta</span> with arugula and apple, served with fries $16</div>
      <div class="dish"><span class="dish-name">Beer Battered Fish &amp; Chips</span> $18</div>
    </div>
  </article>

</main>
</body>
</html>
```